Postcard Design

New property management company. We manage vacation rental properties on a gulf coast island. This post card will be designed to attract home owners to sign on with us to manage their property (s). We want to convay the message that we will take care if everything needed to maintain value in their investment property to attracting the right sort of renters as well as take care of accounting. We can do this because of our sister relationship with a local contractor and the fact that we are a small company planning to stay that way.
We would like to have a call to action offer of "reduced rates for new clients this month". Please fill free to play with those words. Make is snassy!
Updates

We have some good submissions. I am not sure we have found the "one" yet. We would like some work done with our "reduced rates" phrase. Try different words. It needs to be the most notices sentence. With our phone number being the second line that pops out. Please don't use paragraphs from out website. Phrases are fine. Thank you for your hard work. We look forward to seeing more designs.

Thank you all for your submissions. I appreciate your time.

Target Market(s)

Investment Property Owners from all over Texas, California, Colorado and most Southern States. Usually med to upper income and 35 +

Industry/Entity Type

Property Management

Requirements
Must have
• Catch line " relax- we'll take care of it"
Offer

Our Logo and information

Front and back small post card with return address in left corner and room for mailing label.
Nice to have
• Eye catching!

Noticeable offer

```html
<!DOCTYPE html>
<html lang="en">
<head>
<meta charset="utf-8">
<title>Saltwind Rentals – Postcard</title>
<link rel="stylesheet" href="https://fonts.googleapis.com/css2?family=Libre+Baskerville:wght@400;700&family=Lato:wght@400;700&family=Dancing+Script:wght@500&display=swap">
<style>
  :root {
    --navy: #1f2a6b;
    --blue: #2f45a6;
    --red: #e0332c;
    --orange-red: #f04a1f;
    --ink: #1c1c1c;
    --paper: #ffffff;
    --paper-shade: #e9e9ec;
    --backdrop: #d9dadd;
    --sand-light: #b9a47e;
    --sand-dark: #6e5c40;
  }
  * { box-sizing: border-box; margin: 0; padding: 0; }
  html, body {
    width: 792px; height: 1200px; overflow: hidden;
    background: var(--backdrop);
  }
  .canvas { position: relative; width: 792px; height: 1200px; }

  .card {
    position: absolute; left: 76px; width: 640px; height: 500px;
    background: linear-gradient(160deg, var(--paper) 40%, var(--paper-shade));
    box-shadow: 0 4px 14px rgba(0,0,0,.25);
    overflow: hidden;
  }
  .card-front { top: 45px; }
  .card-back { top: 635px; }
  .card svg.art { position: absolute; inset: 0; }

  /* Front */
  .brand {
    position: absolute; right: 32px; top: 52px; text-align: center;
  }
  .brand-name {
    font-family: "Libre Baskerville", serif; font-weight: 400;
    font-size: 30px; color: var(--red); letter-spacing: 1px; line-height: 1;
  }
  .brand-tag {
    font-family: "Libre Baskerville", serif; font-size: 10.5px;
    color: var(--navy); font-style: italic; margin-top: 6px;
  }
  .headline {
    position: absolute; right: 32px; bottom: 50px; text-align: right;
    font-family: "Libre Baskerville", serif; font-weight: 700;
  }
  .headline-main {
    font-size: 62px; color: var(--red); line-height: 1;
    text-shadow: 0 2px 3px rgba(0,0,0,.35);
  }
  .headline-sub {
    font-size: 25px; color: var(--paper); margin-top: 8px; letter-spacing: .3px;
    font-weight: 400;
  }

  /* Back */
  .about-tab {
    position: absolute; left: 0; top: 38px; width: 150px; height: 34px;
    background: var(--red); border-radius: 0 8px 8px 0;
    color: var(--paper); font-family: "Libre Baskerville", serif; font-size: 17px;
    display: flex; align-items: center; padding-left: 20px;
  }
  .about-text {
    position: absolute; left: 20px; top: 88px; width: 340px;
    font-family: "Lato", sans-serif; font-size: 13px; line-height: 1.38; color: var(--ink);
  }
  .offer {
    position: absolute; left: 20px; top: 202px;
    font-family: "Libre Baskerville", serif; font-weight: 700; line-height: 1.2;
  }
  .offer-main { font-size: 22.5px; color: var(--orange-red); }
  .offer-sub { font-size: 18.5px; color: var(--ink); }

  .gallery { position: absolute; left: 18px; top: 280px; display: flex; gap: 28px; }
  .gallery-item {
    width: 94px; height: 94px; border-radius: 50%;
    border: 4px solid #f3f3f3; box-shadow: 0 2px 6px rgba(0,0,0,.35);
  }
  .photo-boat { background: radial-gradient(circle at 50% 55%, #c8343a, #7a8fa8 70%); }
  .photo-pier { background: radial-gradient(circle at 50% 60%, #9a8a72, #8fb0cf 75%); }
  .photo-bird { background: radial-gradient(circle at 50% 55%, #b9b2a4, #3f6f9c 70%); }

  .contacts {
    position: absolute; left: 20px; top: 398px; list-style: none;
    font-family: "Lato", sans-serif; font-weight: 700; font-size: 14.5px; color: var(--ink);
  }
  .contacts li { display: flex; align-items: center; gap: 10px; height: 25px; }
  .contacts svg { width: 14px; height: 14px; fill: var(--red); }

  .stamp-box {
    position: absolute; left: 530px; top: 56px; width: 82px; height: 96px;
    border: 1px solid #444;
  }
  .address-line {
    position: absolute; left: 428px; width: 182px; height: 0; border-top: 1.5px solid #333;
  }
</style>
</head>
<body>
<div class="canvas">

  <!-- Front -->
  <section class="card card-front">
    <svg class="art" viewBox="0 0 640 500" width="640" height="500">
      <defs>
        <linearGradient id="sand" x1="0" y1="0" x2="1" y2="1">
          <stop offset="0" stop-color="var(--sand-light)"/>
          <stop offset="1" stop-color="var(--sand-dark)"/>
        </linearGradient>
        <linearGradient id="sea-band" x1="0" y1="0" x2="1" y2="0">
          <stop offset="0" stop-color="var(--navy)"/>
          <stop offset=".5" stop-color="var(--blue)"/>
          <stop offset="1" stop-color="var(--navy)"/>
        </linearGradient>
      </defs>
      <path role="img" aria-label="Footprints in beach sand with sea foam at the edge"
            d="M0,222 L162,58 L640,300 L640,500 L0,500 Z" fill="url(#sand)"/>
      <path d="M0,220 C40,240 110,300 150,360 C170,400 120,430 0,440 Z" fill="#e8eef4" opacity=".9"/>
      <!-- chimney -->
      <path d="M52,60 L92,60 L92,120 L52,160 Z" fill="var(--red)"/>
      <!-- roof lines -->
      <path d="M0,205 L162,40 L640,282" fill="none" stroke="var(--navy)" stroke-width="12"/>
      <path d="M0,222 L162,58 L640,300" fill="none" stroke="var(--red)" stroke-width="10"/>
      <!-- waves -->
      <path d="M0,390 C140,350 300,290 640,296 L640,500 L0,500 Z" fill="var(--paper)"/>
      <path d="M0,408 C150,368 310,306 640,312 L640,326 C320,324 170,384 0,426 Z" fill="var(--red)"/>
      <path d="M0,436 C170,398 340,338 640,340 L640,500 L0,500 Z" fill="url(#sea-band)"/>
    </svg>
    <div class="brand">
      <div class="brand-name">SALTWIND</div>
      <div class="brand-tag">Rentals and Management Company</div>
    </div>
    <div class="headline">
      <div class="headline-main">RELAX</div>
      <div class="headline-sub">WE'LL TAKE CARE OF IT</div>
    </div>
  </section>

  <!-- Back -->
  <section class="card card-back">
    <svg class="art" viewBox="0 0 640 500" width="640" height="500">
      <path d="M340,0 C420,120 400,300 330,500 L372,500 C430,300 450,120 388,0 Z" fill="var(--navy)"/>
      <path d="M322,0 C395,120 380,300 312,500" fill="none" stroke="var(--red)" stroke-width="4"/>
    </svg>

    <div class="about-tab">ABOUT US</div>
    <p class="about-text">Saltwind Rentals is a small company that takes pride in maintaining properties like they are our own. Every home that we manage is given special attention. Our goal is for your renters to come back again and again. Your property will continue to increase in value under our care.</p>

    <div class="offer">
      <div class="offer-main">REDUCED RATES FOR</div>
      <div class="offer-sub">NEW CLIENTS THIS MONTH</div>
    </div>

    <div class="gallery">
      <div class="gallery-item photo-boat" role="img" aria-label="Red and white harbor ferry boat"></div>
      <div class="gallery-item photo-pier" role="img" aria-label="Wooden fishing pier building over the water"></div>
      <div class="gallery-item photo-bird" role="img" aria-label="Pelican standing by the water"></div>
    </div>

    <ul class="contacts">
      <li><svg viewBox="0 0 24 24"><path d="M6.6 10.8a15 15 0 0 0 6.6 6.6l2.2-2.2a1 1 0 0 1 1-.25 11.4 11.4 0 0 0 3.6.57 1 1 0 0 1 1 1V20a1 1 0 0 1-1 1A17 17 0 0 1 3 4a1 1 0 0 1 1-1h3.5a1 1 0 0 1 1 1c0 1.25.2 2.45.57 3.57a1 1 0 0 1-.25 1z"/></svg>+1 (361) 555-0142</li>
      <li><svg viewBox="0 0 24 24"><path d="M12 3 2 12h3v9h5v-6h4v6h5v-9h3z"/></svg>Gull Harbor, TX 78300</li>
      <li><svg viewBox="0 0 24 24"><path d="M12 2a10 10 0 1 0 0 20 10 10 0 0 0 0-20zm6.9 6h-2.9a15.7 15.7 0 0 0-1.4-3.6A8 8 0 0 1 18.9 8zM12 4a14 14 0 0 1 1.9 4h-3.8A14 14 0 0 1 12 4zM4.3 14a8 8 0 0 1 0-4h3.4a16 16 0 0 0 0 4zm.8 2h2.9a15.7 15.7 0 0 0 1.4 3.6A8 8 0 0 1 5.1 16zM8 8H5.1a8 8 0 0 1 4.3-3.6A15.7 15.7 0 0 0 8 8zm4 12a14 14 0 0 1-1.9-4h3.8A14 14 0 0 1 12 20zm2.3-6H9.7a14.7 14.7 0 0 1 0-4h4.6a14.7 14.7 0 0 1 0 4zm.3 5.6a15.7 15.7 0 0 0 1.4-3.6h2.9a8 8 0 0 1-4.3 3.6zM16.3 14a16 16 0 0 0 0-4h3.4a8 8 0 0 1 0 4z"/></svg>www.saltwindrentals.com</li>
    </ul>

    <div class="stamp-box"></div>
    <div class="address-line" style="top:265px"></div>
    <div class="address-line" style="top:302px"></div>
    <div class="address-line" style="top:341px"></div>
  </section>

</div>
</body>
</html>
```